CD front and back cover and CD disk. Front includes design elements of the attached band photo, the name of the band (Quiet Harbor Lanterns) and the album name (Paper Anchors?). I've attached a photshoped band photo and an original image. I like the color palette of the photoshoped pix but it may be too dark. So I've attached the original pix, that could be photoshoped. Music is alternative rock. See website qhlTunes.com and the EPK on the site. Songs are not up for this CD yet. Concept - modern, clean, NO gothic rock font or style of any kind.

Back cover needs songs, website and contact as follows:

Hold Ember (Electric)
Linger
Bent and Broken
Meridian
You Sink You Swim
Lean Past You
Hold Ember (Acoustic)
Room To Roam
The Tide
Push Too Far

qhlTunes.com
info@qhlTunes.com
- the actual cd needs the same as above
- use the DiscNook template Sleeve S240 

• Back cover needs the song titles, website, contact info and copyright as follows:
Hold Ember (electric)
Linger
Bent and Broken
Meridian
You Sink You Swim
Lean Past You
Hold Ember (acoustic)
Room To Roam
The Tide
Push Too Far

qhlTune.com
info@qhlTunes.com
Copyright © 2013 Quiet Harbor Lanterns | All Rights Reserved
Also - dimensions for CD Sleeve S240 on discnook.com
Also - CD disk to contain all of the above

```html
<!DOCTYPE html>
<html lang="en">
<head>
<meta charset="utf-8">
<title>Quiet Harbor Lanterns – Paper Anchors? CD Sleeve</title>
<link rel="stylesheet" href="https://fonts.googleapis.com/css2?family=Open+Sans:wght@400;700&family=Oswald:wght@500&family=Staatliches&display=swap">
<style>
  :root {
    --paper: #ffffff;
    --label-grey: #a3a3a3;
    --ink: #111111;
    --sleeve-black: #141414;
    --sleeve-dark: #262626;
    --moss: #93a56c;
    --moss-disc: #8c9d72;
    --moss-disc-dark: #7d8e63;
    --white: #f4f4f0;
    --trim: #333333;
    --tag-accent: #e23b8b;
  }
  * { box-sizing: border-box; margin: 0; padding: 0; }
  html, body { width: 1200px; height: 1200px; overflow: hidden; background: var(--paper); }
  .sheet { position: relative; width: 1200px; height: 1200px; background: var(--paper); }

  .panel-label {
    position: absolute; top: 26px; width: 300px; text-align: center;
    font-family: "Open Sans", Arial, sans-serif; font-weight: 700;
    font-size: 29px; color: var(--label-grey);
  }
  .panel-label--back { left: 190px; }
  .panel-label--front { left: 715px; }

  .trim-marks { position: absolute; inset: 0; pointer-events: none; }

  .back-cover {
    position: absolute; left: 70px; top: 64px; width: 536px; height: 536px;
    background: radial-gradient(ellipse at 50% 40%, var(--sleeve-dark) 0%, var(--sleeve-black) 75%);
    overflow: hidden;
  }
  .tracklist {
    position: absolute; left: 0; right: 0; top: 166px; list-style: none; text-align: center;
    font-family: "Staatliches", "Oswald", sans-serif; font-size: 17px; line-height: 21px;
    letter-spacing: 1.5px; color: var(--moss);
  }
  .back-cover__footer {
    position: absolute; left: 0; right: 0; bottom: 0; height: 26px;
    font-family: "Open Sans", Arial, sans-serif; font-weight: 700; font-size: 8px;
    color: var(--white); white-space: nowrap;
  }
  .back-cover__copyright { position: absolute; left: 96px; top: 8px; }
  .back-cover__contact { position: absolute; right: 14px; top: 8px; }
  .back-cover__contact span + span { margin-left: 12px; }

  .front-cover {
    position: absolute; left: 604px; top: 60px; width: 534px; height: 536px;
    background: var(--ink); padding: 8px;
  }
  .front-cover__photo {
    position: absolute; inset: 8px;
    background: linear-gradient(100deg, #3a3a3a 0%, #1b1b1b 35%, #4a4a4a 60%, #232323 80%, #3b3b3b 100%);
  }
  .band-name {
    position: absolute; left: 150px; top: 176px;
    font-family: "Oswald", sans-serif; font-weight: 500; font-size: 48px;
    line-height: 54px; letter-spacing: 8px; color: var(--moss); text-transform: uppercase;
  }
  .album-title {
    position: absolute; left: 152px; top: 356px;
    font-family: "Staatliches", sans-serif; font-size: 22px; letter-spacing: 2px; color: var(--white);
  }

  .template-tag {
    position: absolute; left: 82px; top: 606px; width: 126px; height: 50px;
    border: 1px solid var(--trim); background: var(--paper);
  }
  .template-tag__mark {
    position: absolute; left: 6px; top: 12px; width: 24px; height: 24px;
    border: 3px solid var(--tag-accent); border-radius: 3px;
  }
  .template-tag__code {
    position: absolute; left: 38px; top: 3px; width: 84px; text-align: center;
    font-family: "Open Sans", Arial, sans-serif; font-weight: 700; font-size: 11px; color: var(--ink);
  }
  .template-tag__note {
    position: absolute; left: 38px; top: 20px; width: 84px; text-align: center;
    font-family: "Open Sans", Arial, sans-serif; font-size: 6px; line-height: 8px; color: var(--ink);
  }
  .paste-note {
    position: absolute; left: 216px; top: 640px;
    font-family: "Open Sans", Arial, sans-serif; font-weight: 700; font-size: 7px; color: var(--ink);
  }

  .disc { position: absolute; left: 322px; top: 684px; width: 500px; height: 500px; }
  .disc-tracklist {
    position: absolute; left: 388px; top: 783px; list-style: none;
    font-family: "Staatliches", "Oswald", sans-serif; font-size: 15px; line-height: 20.5px;
    letter-spacing: 0.5px; color: var(--white);
  }
</style>
</head>
<body>
<main class="sheet">
  <div class="panel-label panel-label--back">Back Cover</div>
  <div class="panel-label panel-label--front">Front Cover</div>

  <svg class="trim-marks" width="1200" height="1200" viewBox="0 0 1200 1200" aria-hidden="true">
    <g stroke="var(--trim)" stroke-width="1.5">
      <line x1="40" y1="60" x2="1165" y2="60"/>
      <line x1="78" y1="30" x2="78" y2="60"/>
      <line x1="606" y1="30" x2="606" y2="60"/>
      <line x1="1138" y1="30" x2="1138" y2="60"/>
      <line x1="40" y1="588" x2="68" y2="588"/>
      <line x1="1138" y1="588" x2="1165" y2="588"/>
      <line x1="606" y1="596" x2="606" y2="620"/>
      <line x1="1138" y1="596" x2="1138" y2="620"/>
    </g>
  </svg>

  <section class="back-cover">
    <ul class="tracklist">
      <li>Hold Ember (Electric)</li>
      <li>Linger</li>
      <li>Bent and Broken</li>
      <li>Meridian</li>
      <li>You Sink You Swim</li>
      <li>Lean Past You</li>
      <li>Hold Ember (Acoustic)</li>
      <li>Room To Roam</li>
      <li>The Tide</li>
      <li>Push Too Far</li>
    </ul>
    <div class="back-cover__footer">
      <span class="back-cover__copyright">Copyright © 2013 Quiet Harbor Lanterns | All Rights Reserved</span>
      <span class="back-cover__contact"><span>info@qhlTunes.com</span><span>qhlTunes.com</span></span>
    </div>
  </section>

  <section class="front-cover">
    <div class="front-cover__photo" role="img" aria-label="Black and white band photo of the four members standing in a dark room"></div>
    <h1 class="band-name">Quiet<br>Harbor<br>Lanterns</h1>
    <p class="album-title">Paper Anchors?</p>
  </section>

  <div class="template-tag">
    <span class="template-tag__mark"></span>
    <div class="template-tag__code">S240</div>
    <div class="template-tag__note">Sleeve S240<br>Insert panel guide</div>
  </div>
  <div class="paste-note">PASTE ON TAG HERE</div>

  <svg class="disc" viewBox="0 0 500 500" aria-label="CD disc label">
    <defs>
      <radialGradient id="disc-fill" cx="45%" cy="40%" r="65%">
        <stop offset="0%" stop-color="var(--moss-disc)"/>
        <stop offset="100%" stop-color="var(--moss-disc-dark)"/>
      </radialGradient>
      <path id="disc-rim" d="M22,250 A228,228 0 0 0 478,250"/>
    </defs>
    <circle cx="250" cy="250" r="248" fill="url(#disc-fill)"/>
    <circle cx="250" cy="250" r="46" fill="#e8ece2"/>
    <circle cx="250" cy="250" r="40" fill="var(--paper)"/>
    <text font-family="Open Sans, Arial, sans-serif" font-weight="700" font-size="12" fill="var(--white)">
      <textPath href="#disc-rim" startOffset="38%" text-anchor="middle">Copyright © 2013 Quiet Harbor Lanterns | All Rights Reserved</textPath>
    </text>
    <g font-family="Open Sans, Arial, sans-serif" font-weight="700" font-size="11" fill="var(--white)" text-anchor="middle">
      <text transform="translate(442 245) rotate(-78)">qhlTunes.com</text>
      <text transform="translate(458 248) rotate(-78)">info@qhlTunes.com</text>
    </g>
  </svg>
  <ul class="disc-tracklist">
    <li>Hold Ember (Electric)</li>
    <li>Linger</li>
    <li>Bent and Broken</li>
    <li>Meridian</li>
    <li>You Sink You Swim</li>
    <li>Lean Past You</li>
    <li>Hold Ember (Acoustic)</li>
    <li>Room To Roam</li>
    <li>The Tide</li>
    <li>Push Too Far</li>
  </ul>
</main>
</body>
</html>
```